Northgate Signal Shield LLC

Need help designing a web page for an alarm company. I want to promote my business.

Target Market(s)

Residential and commercial clients

Industry/Entity Type

Security Service

Coding

Coded - Design and coding required

Number of Pages Required

2 page

Font styles to use
Sans Serif

Requirements
Must have
• I would llike my logo displayed on the page. I would like my slogan displayed as well
´´A GREAT PLACE FOR YOUR SECURITY NEEDS´´
We are licensed and insured
Company phone number 713-555-0142
Company hours: Monday-Friday 8am-5pm Company address: P.O. Box 419 Crosby, TX 77064 over 25 years experience
Email info. Northgatess@ferntopmail.com
Company license #K52948316
Fire license# TMV-6614027
JLP-8170326
We offer alarm monitoring,security cameras, access control,gate openers, home theater systems, covert camera installations, FIre alarm installation and monitoring
Nice to have
• We offer security at competitive prices.
Get customer information for a free quote similar to brx website.
Should not have
• No prices listed on website

```html
<!DOCTYPE html>
<html lang="en">
<head>
<meta charset="utf-8">
<title>Northgate Signal Shield</title>
<link href="https://fonts.googleapis.com/css2?family=Krona+One&family=Poppins:wght@400;500;600;700&display=swap" rel="stylesheet">
<style>
:root{
  --red:#e0161f;
  --red-dark:#c10f17;
  --ink:#111111;
  --night:#0d1524;
  --white:#ffffff;
  --grey:#6b6b6b;
  --line:#d9d9d9;
  --sky-top:#1a3d9a;
  --sky-mid:#2a5fc4;
  --glow:#c77a2a;
}
*{margin:0;padding:0;box-sizing:border-box}
html,body{width:1200px;height:2781px;overflow:hidden;background:var(--white);font-family:"Poppins",sans-serif;color:var(--ink)}
.page{position:relative;width:1200px;height:2781px;overflow:hidden}
.abs{position:absolute}
.display{font-family:"Krona One",sans-serif}

/* hero */
.hero-bg{left:0;top:0;width:1200px;height:660px;background:linear-gradient(180deg,var(--sky-top) 0%,var(--sky-mid) 38%,#24407a 58%,var(--glow) 80%,#3a2a40 100%)}
.hero-cut{left:0;top:540px}
.logo{left:234px;top:40px;display:flex;align-items:center;gap:10px}
.logo-mark{width:40px;height:40px;border-radius:50%;background:var(--red)}
.logo-name{font-family:"Krona One",sans-serif;font-size:26px;color:var(--red)}
.call{left:670px;top:34px;display:flex;align-items:center;gap:10px;color:var(--white)}
.call-icon{width:34px;height:34px;border-radius:50%;background:var(--red);display:flex;align-items:center;justify-content:center}
.call small{display:block;font-size:12px;font-weight:600;line-height:1.2}
.call strong{display:block;font-size:16px;font-weight:700;line-height:1.2}
.btn{background:var(--red);color:var(--white);font-weight:600;text-align:center}
.top-quote{left:840px;top:30px;width:125px;height:36px;line-height:36px;font-size:11px}
.nav{left:491px;top:91px;display:flex;gap:32px;font-size:12px;font-weight:600;color:var(--white)}
.hero-title{left:234px;top:236px;width:390px;font-size:43px;line-height:52px;color:var(--white);white-space:nowrap}
.hero-slogan{left:234px;top:294px;width:390px;font-size:20px;line-height:31px;color:var(--white)}
.hero-meta{left:234px;top:364px;width:390px;font-size:13px;font-weight:600;line-height:20px;color:var(--white)}
.product-photo{left:262px;top:420px;width:330px;height:242px;border-radius:40px;background:radial-gradient(circle at 45% 45%,#ffffff 0%,#e6e8eb 60%,rgba(220,222,226,0) 100%)}
.quote-box{left:647px;top:159px;width:318px;height:396px;background:rgba(255,255,255,.93);border-radius:6px;padding:22px 12px}
.quote-box h2{font-family:"Krona One",sans-serif;font-size:19px;text-align:center;margin-bottom:18px}
.field{height:44px;border:1px solid var(--line);border-radius:3px;background:var(--white);font-size:11px;color:var(--grey);padding:14px 16px;margin-bottom:13px}
.field-row{display:flex;gap:12px}
.field-row .field{flex:1}
.legal{font-size:8.6px;line-height:15px;color:#333;margin:2px 0 10px}
.submit{height:44px;line-height:44px;font-size:15px;border-radius:3px}

/* section titles */
.sec-title{left:0;width:1200px;display:flex;justify-content:center;align-items:center;gap:20px}
.sec-title span.rule{display:block;width:76px;height:2px;background:var(--ink)}
.sec-title h2{font-family:"Krona One",sans-serif;font-size:23px}

/* offers */
.offer{width:231px}
.offer .photo{height:153px;background:linear-gradient(135deg,#cfd6de,#8d98a6)}
.offer .badge{position:absolute;left:15px;top:116px;width:60px;height:60px;border-radius:50%;background:var(--white);border:2px solid var(--red);display:flex;align-items:center;justify-content:center}
.offer p{margin-top:40px;font-size:13px;font-weight:600;line-height:19px}

/* services */
.svc-bg{left:0;top:1318px}
.svc-title h2{color:var(--white)}
.svc-title span.rule{background:var(--white)}
.svc-col{width:320px;color:var(--white)}
.svc-col h3{font-family:"Poppins",sans-serif;font-weight:700;font-size:25px;letter-spacing:2px;margin:14px 0 12px}
.svc-col p{font-size:11.6px;line-height:17.5px;letter-spacing:.5px}
.svc-btn{left:538px;top:1796px;width:124px;height:36px;line-height:36px;font-size:11px}

/* news */
.news{width:231px}
.news .photo{height:180px;background:linear-gradient(135deg,#e4e9ee,#9aa6b2)}
.news .card{position:relative;margin-top:-30px;width:203px;background:var(--white);padding:12px 0 0 22px}
.news .date{font-size:8.5px;font-weight:600;color:var(--grey)}
.news h4{margin-top:10px;border-left:2px solid var(--red);padding-left:12px;font-size:10px;font-weight:700;line-height:19px}
.news p{padding-left:14px;margin-top:8px;font-size:10.5px;line-height:15px;color:#333}

/* footer */
.foot-bg{left:0;top:2428px}
.foot-col h5{font-size:10px;font-weight:700;color:var(--white);margin-bottom:18px}
.foot-col li{list-style:none;font-size:9px;color:var(--white);line-height:12px;margin-bottom:10px;display:flex;gap:8px}
.dot{width:9px;flex:none;color:var(--red)}
.social{display:flex;gap:8px;margin-bottom:14px}
.social span{width:26px;height:26px;border:1.5px solid var(--white);border-radius:50%}
.copyright{left:0;top:2752px;width:1200px;text-align:center;font-size:9px;color:#8a8a8a}
.skyline{left:0;top:2712px;width:1200px;height:69px;background:linear-gradient(180deg,#000 0%,#161616 100%)}
</style>
</head>
<body>
<div class="page">

  <!-- hero -->
  <div class="abs hero-bg" role="img" aria-label="Night city skyline over water with reflected lights"></div>
  <svg class="abs hero-cut" width="1200" height="130" viewBox="0 0 1200 130">
    <polygon points="0,28 600,112 1200,0 1200,130 0,130" fill="#ffffff"/>
    <polygon points="550,105 600,112 1200,0 1200,6 600,120" fill="#e0161f"/>
  </svg>

  <div class="abs logo"><span class="logo-mark"></span><span class="logo-name">NORTHGATE</span></div>
  <div class="abs call">
    <span class="call-icon"><svg width="16" height="16" viewBox="0 0 24 24"><path fill="#fff" d="M6.6 10.8a15 15 0 0 0 6.6 6.6l2.2-2.2c.3-.3.7-.4 1-.2 1.1.4 2.3.6 3.6.6.6 0 1 .4 1 1V20c0 .6-.4 1-1 1A17 17 0 0 1 3 4c0-.6.4-1 1-1h3.5c.6 0 1 .4 1 1 0 1.3.2 2.5.6 3.6.1.3 0 .7-.2 1z"/></svg></span>
    <span><small>Call Us:</small><strong>713-555-0142</strong></span>
  </div>
  <div class="abs btn top-quote">GET A FREE QUOTE</div>
  <nav class="abs nav"><span>HOME</span><span>ABOUT US</span><span>SERVICES</span><span>PRODUCTS</span><span>BLOG</span><span>CONTACT US</span></nav>

  <h1 class="abs hero-title display">NORTHGATE</h1>
  <p class="abs hero-slogan display">A GREAT PLACE FOR YOUR<br>SECURITY NEEDS</p>
  <p class="abs hero-meta">Licensed and insured &middot; Over 25 years experience</p>
  <div class="abs product-photo" role="img" aria-label="Two white wireless security cameras"></div>

  <form class="abs quote-box">
    <h2>GET A FREE QUOTE</h2>
    <div class="field">Name</div>
    <div class="field">Email</div>
    <div class="field-row"><div class="field">Phone</div><div class="field">ZIP</div></div>
    <p class="legal">By clicking the 'Great a Free Quote' button below. I agree that an BRX specialist may contact me via text message or phone calls to the phone number provided by me using automated technology about BRX offers and consent is not required to make a purchase. Your information i collected and used in accordance with our privacy policy.</p>
    <div class="btn submit">GET A FREE QUOTE</div>
  </form>

  <!-- offers -->
  <div class="abs sec-title" style="top:722px"><span class="rule"></span><h2>WE OFFERS</h2><span class="rule"></span></div>

  <div class="abs offer" style="left:234px;top:788px"><div class="photo" role="img" aria-label="Dome security camera in a modern lobby"></div>
    <div class="badge"><svg width="28" height="28" viewBox="0 0 28 28" fill="none" stroke="#e0161f" stroke-width="2"><rect x="4" y="7" width="16" height="8" rx="1"/><path d="M20 11h4M10 15v6h-4"/></svg></div>
    <p>Security Cameras</p></div>
  <div class="abs offer" style="left:484px;top:788px"><div class="photo" role="img" aria-label="Finger pressing an access control keypad"></div>
    <div class="badge"><svg width="28" height="28" viewBox="0 0 28 28" fill="none" stroke="#e0161f" stroke-width="2"><rect x="9" y="4" width="6" height="20"/><path d="M15 10l8 4"/></svg></div>
    <p>Access Control</p></div>
  <div class="abs offer" style="left:734px;top:788px"><div class="photo" role="img" aria-label="Iron driveway gate in front of a house"></div>
    <div class="badge"><svg width="28" height="28" viewBox="0 0 28 28"><rect x="6" y="6" width="7" height="16" fill="#e0161f"/><rect x="16" y="4" width="3" height="20" fill="none" stroke="#e0161f" stroke-width="2"/></svg></div>
    <p>Gate Openers</p></div>

  <div class="abs offer" style="left:234px;top:1025px"><div class="photo" role="img" aria-label="Home theater room with sofa and screen"></div>
    <div class="badge"><svg width="32" height="28" viewBox="0 0 32 28" fill="none" stroke="#e0161f" stroke-width="2"><rect x="3" y="8" width="8" height="12"/><rect x="21" y="8" width="8" height="12"/><rect x="12" y="12" width="8" height="8"/></svg></div>
    <p>Home Theater Systems</p></div>
  <div class="abs offer" style="left:484px;top:1025px"><div class="photo" role="img" aria-label="Small covert camera held in a palm"></div>
    <div class="badge"><svg width="28" height="28" viewBox="0 0 28 28" fill="none" stroke="#e0161f" stroke-width="2"><rect x="4" y="4" width="20" height="20" rx="3"/><circle cx="14" cy="14" r="5"/></svg></div>
    <p>Covert Camera Installations</p></div>
  <div class="abs offer" style="left:734px;top:1025px"><div class="photo" role="img" aria-label="Operator at a monitoring station with screens"></div>
    <div class="badge"><svg width="28" height="28" viewBox="0 0 28 28" fill="none" stroke="#e0161f" stroke-width="2"><path d="M8 20v-7a6 6 0 0 1 12 0v7zM5 20h18M12 23h4"/></svg></div>
    <p>Fire Alaram Installation and<br>Monitoring</p></div>

  <!-- services -->
  <svg class="abs svc-bg" width="1200" height="604" viewBox="0 0 1200 604">
    <defs>
      <linearGradient id="svcRed" x1="0" y1="0" x2="1" y2="1"><stop offset="0" stop-color="#ee2a30"/><stop offset="1" stop-color="#d3141c"/></linearGradient>
      <linearGradient id="svcDark" x1="0" y1="0" x2="1" y2="1"><stop offset="0" stop-color="#1b2536"/><stop offset="1" stop-color="#05080e"/></linearGradient>
    </defs>
    <polygon points="0,76 600,0 600,604 0,518" fill="url(#svcRed)"/>
    <polygon points="600,0 1200,76 1200,518 600,604" fill="url(#svcDark)"/>
  </svg>
  <div class="abs sec-title svc-title" style="top:1413px"><span class="rule"></span><h2>OUR SERVICES</h2><span class="rule"></span></div>

  <div class="abs svc-col" style="left:234px;top:1500px">
    <svg width="22" height="40" viewBox="0 0 22 40" fill="none" stroke="#fff" stroke-width="2"><rect x="2" y="10" width="18" height="28" rx="2"/><path d="M6 10V2"/><rect x="6" y="15" width="10" height="7"/></svg>
    <h3>AUDIO SECURITY</h3>
    <p>Lorem ipsum dolor sit amet, consectetur adipiscing elit. Nunc accumsan, ex nec condimentum vestibu-lum, lacus felis vehicula quam, in imperdiet elit metus ut dolor. Pellentesque sed mattis tortor, sed viverra dolor. Maecenas a dui dictum sapien luctus venenatis non vitae ex. Nunc ut elementum eros. Ut molestie velit et vulputate pharetra. Pellentesque justo est, ve-hicula vel ligula vel, eleifend faucibus felis.</p>
  </div>
  <div class="abs svc-col" style="left:653px;top:1500px">
    <svg width="40" height="40" viewBox="0 0 40 40" fill="none" stroke="#fff" stroke-width="2"><rect x="10" y="6" width="26" height="10" transform="rotate(-15 23 11)"/><path d="M18 18v8H8M4 20v14"/></svg>
    <h3>VIDEO SECURITY</h3>
    <p>Lorem ipsum dolor sit amet, consectetur adipiscing elit. Nunc accumsan, ex nec condimentum vestibu-lum, lacus felis vehicula quam, in imperdiet elit metus ut dolor. Pellentesque sed mattis tortor, sed viverra dolor. Maecenas a dui dictum sapien luctus venenatis non vitae ex. Nunc ut elementum eros. Ut molestie velit et vulputate pharetra. Pellentesque justo est, ve-hicula vel ligula vel, eleifend faucibus felis.</p>
  </div>
  <div class="abs btn svc-btn">CONTACT US</div>

  <!-- news -->
  <div class="abs sec-title" style="top:1997px"><span class="rule"></span><h2>LATEST NEWS</h2><span class="rule"></span></div>

  <div class="abs news" style="left:234px;top:2063px"><div class="photo" role="img" aria-label="Technician installing a ceiling camera"></div>
    <div class="card"><div class="date">26 JULY 2020</div><h4>LOREM IPSUM DOLOR SIT AMET,<br>CONSECTETUR ADIPISCING</h4><p>Pellentesque eu placerat purus, sollicitudin elementum tellus. Proin at mauris tortor.</p></div></div>
  <div class="abs news" style="left:484px;top:2063px"><div class="photo" role="img" aria-label="Bullet security camera mounted on a wall"></div>
    <div class="card"><div class="date">26 JULY 2020</div><h4>LOREM IPSUM DOLOR SIT AMET,<br>CONSECTETUR ADIPISCING</h4><p>Pellentesque eu placerat purus, sollicitudin elementum tellus. Proin at mauris tortor.</p></div></div>
  <div class="abs news" style="left:734px;top:2063px"><div class="photo" role="img" aria-label="Desk with multiple surveillance monitors"></div>
    <div class="card"><div class="date">26 JULY 2020</div><h4>LOREM IPSUM DOLOR SIT AMET,<br>CONSECTETUR ADIPISCING</h4><p>Pellentesque eu placerat purus, sollicitudin elementum tellus. Proin at mauris tortor.</p></div></div>

  <!-- footer -->
  <svg class="abs foot-bg" width="1200" height="353" viewBox="0 0 1200 353">
    <polygon points="0,94 600,0 1200,94 1200,353 0,353" fill="#e0161f"/>
    <polygon points="0,100 600,10 1200,100 1200,353 0,353" fill="#000000"/>
  </svg>
  <div class="abs skyline" role="img" aria-label="Dark city skyline silhouette"></div>

  <div class="abs foot-col" style="left:235px;top:2542px;width:210px">
    <h5>CONTACT INFO</h5>
    <ul>
      <li><span class="dot">&#9742;</span>713-555-0142</li>
      <li><span class="dot">&#9993;</span>Northgatess@ferntopmail.com</li>
      <li><span class="dot">&#9679;</span>P.O. Box 419 Crosby, TX 77064</li>
      <li><span class="dot">&#9719;</span>Monday-Friday 8am-5pm</li>
      <li><span class="dot">&#10003;</span>Licensed and insured &middot; 25+ years</li>
    </ul>
  </div>
  <div class="abs foot-col" style="left:470px;top:2542px">
    <h5>QUICK LINKS</h5>
    <ul><li>About us</li><li>Gallery</li><li>Blog</li><li>Contact Us</li></ul>
  </div>
  <div class="abs foot-col" style="left:588px;top:2542px">
    <h5>SERVICES</h5>
    <ul><li>Alarm Monitoring</li><li>Security Cameras</li><li>Access Control</li><li>Gate Openers</li></ul>
  </div>
  <div class="abs foot-col" style="left:695px;top:2577px">
    <ul><li>Home Theater Systems</li><li>Fire alarm installation<br>and monitoring</li></ul>
  </div>
  <div class="abs foot-col" style="left:844px;top:2542px">
    <h5>FOLLOW US</h5>
    <div class="social"><span></span><span></span><span></span><span></span></div>
    <ul><li>Company license #K52948316</li><li>Fire license# TMV-6614027</li><li>JLP-8170326</li></ul>
  </div>
  <p class="abs copyright">Copyright © 2020 Northgate Signal Shield LLC. All Rights Reserved</p>

</div>
</body>
</html>
```